Bluestone Freight

We are a 3PL freight brokerage company looking to create a website to attract new customers. Some ideas on how other freight websites look is located at these links, https://www.marigoldhaulerline.com/services, https://quillmarkcargo.com/freight-brokerage/.
We would like to have a quote feature implemented into this website.

We specialize in heavy-haul, specialized loads, flatbed, and dry vans.

```html
<!DOCTYPE html>
<html lang="en">
<head>
<meta charset="utf-8">
<title>Bluestone Freight</title>
<link href="https://fonts.googleapis.com/css2?family=Poppins:wght@300;400;500;600;700&display=swap" rel="stylesheet">
<style>
:root{
  --ink:#111214;
  --ink-soft:#2b2d30;
  --text:#3b3d40;
  --muted:#8a8d91;
  --line:#d9dadc;
  --paper:#ffffff;
  --mist:#f3f3f4;
  --night:#0b0b0c;
  --footer:#222325;
  --footer-deep:#1a1b1c;
}
*{box-sizing:border-box;margin:0;padding:0}
html,body{width:1200px;height:3001px;overflow:hidden}
body{position:relative;font-family:'Poppins',sans-serif;color:var(--text);background:var(--paper)}
.abs{position:absolute}
a{color:inherit;text-decoration:none}

/* header */
.site-header{left:0;top:0;width:1200px;height:49px;z-index:3;border-bottom:1px solid rgba(255,255,255,.15);background:rgba(20,20,22,.55)}
.brand{left:157px;top:16px;color:#fff;font-weight:600;font-size:14px;letter-spacing:1px;display:flex;align-items:center;gap:7px}
.brand .dot{width:10px;height:10px;background:#fff;border-radius:50%}
.nav{right:196px;top:15px;display:flex;gap:10px;color:#fff;font-size:10.5px}
.nav .phone{margin-left:16px;font-weight:500;display:flex;align-items:center;gap:4px}
.search{right:160px;top:15px}

/* hero */
.hero{left:0;top:0;width:1200px;height:524px;background:linear-gradient(100deg,#3a3b3d 0%,#2a2b2d 40%,#6a6b6d 75%,#9a9b9d 100%)}
.hero::after{content:"";position:absolute;inset:0;background:linear-gradient(180deg,rgba(0,0,0,.1) 60%,rgba(0,0,0,.45))}
.hero-title{left:157px;top:128px;width:420px;color:#fff;font-weight:600;font-size:41px;line-height:47px;z-index:1}
.hero-sub{left:158px;top:283px;width:400px;color:#eee;font-size:15px;line-height:22px;font-weight:300;z-index:1}
.btn{display:inline-flex;align-items:center;justify-content:center;font-weight:600;font-size:10px;letter-spacing:.2px}
.btn-light{background:#fff;color:var(--ink)}
.btn-dark{background:var(--night);color:#fff}
.hero-btn{left:158px;top:347px;width:93px;height:33px;z-index:1}

/* stats */
.stats{left:0;top:524px;width:1200px;height:84px;background:var(--night);display:flex;justify-content:center}
.stat{width:226px;display:flex;align-items:center;justify-content:center;gap:10px;color:#fff;border-right:1px solid #2a2a2c}
.stat:last-child{border-right:0}
.stat b{display:block;font-size:26px;font-weight:600;line-height:28px}
.stat span{font-size:9.5px;color:#ddd}

/* intro */
.intro{left:0;top:646px;width:1200px;text-align:center;color:var(--ink-soft);font-size:25px;font-weight:300;line-height:33px}
.intro strong{font-weight:600;color:var(--ink)}
.feature{top:762px;width:215px}
.feature h3{font-size:15px;font-weight:500;color:var(--ink);margin:14px 0 10px}
.feature p{font-size:11.5px;line-height:17.5px;color:var(--text)}
.feature .tag{margin-top:6px}
.feature-card{left:463px;top:734px;width:278px;height:231px;background:#fff;box-shadow:0 8px 24px rgba(0,0,0,.08);border-bottom:5px solid var(--ink)}

/* pricing */
.price-title{left:237px;top:1080px;width:380px;font-size:26px;line-height:33px;color:var(--ink);font-weight:400}
.contact-row{display:flex;gap:20px;font-size:10.5px;color:var(--ink);font-weight:500}
.contact-row span{display:flex;align-items:center;gap:5px}
.map{left:629px;top:1019px;width:345px;height:332px;background:radial-gradient(ellipse at 55% 50%,#ececed 0%,#f3f3f4 60%,#fafafa 100%)}
.pin{font-size:9px;color:var(--ink);text-align:center}
.map-card{left:600px;top:1172px;width:171px;height:144px;background:#fff;box-shadow:0 6px 20px rgba(0,0,0,.09);padding:12px 14px;font-size:9px;color:var(--ink)}
.map-card h4{font-weight:500;font-size:13px;margin:0 0 10px 17px}
.map-card p{display:flex;gap:6px;margin-bottom:10px;line-height:15px;font-weight:500}

/* value */
.value-title{left:159px;top:1454px;width:380px;font-size:27px;line-height:33px;color:var(--ink);font-weight:400}
.value-list{left:159px;top:1540px;list-style:none;font-size:11.5px;color:var(--ink-soft)}
.value-list li{height:26.2px;display:flex;align-items:center;gap:10px}
.value-list li::before{content:"";width:5px;height:5px;background:var(--ink);border-radius:50%}
.value-shadow{left:600px;top:1450px;width:416px;height:330px;background:var(--night)}
.value-photo{left:623px;top:1427px;width:416px;height:329px;background:linear-gradient(180deg,#a8a9ab 0%,#8c8d8f 45%,#5b5c5e 70%,#3d3e40 100%)}

/* testimonials */
.testi-band{left:0;top:1835px;width:935px;height:268px;background:var(--mist)}
.testi-title{left:160px;top:1866px;font-size:25px;color:var(--ink);font-weight:400}
.view-all{left:997px;top:1875px;font-size:11px;color:var(--ink);text-decoration:underline}
.quote{top:1934px;width:281px;height:201px;background:#fff;box-shadow:0 4px 18px rgba(0,0,0,.06);padding:38px 26px 0}
.quote p{font-size:11px;line-height:17.5px;color:var(--text);height:62px}
.quote hr{border:0;border-top:1px solid var(--line);margin:8px 0 16px}
.quote hr::before{content:"";display:block;width:30px;height:2px;background:var(--ink);margin-top:-1px}
.person{display:flex;align-items:center;gap:16px}
.person .avatar{width:40px;height:40px;border-radius:50%;background:#1f3f7a}
.person b{display:block;font-size:11.5px;font-weight:500;color:var(--ink)}
.person small{font-size:9px;color:var(--muted)}

/* faq */
.faq-title{left:0;top:2186px;width:1200px;text-align:center;font-size:26px;color:var(--ink);font-weight:400}
.faq h4{display:flex;align-items:center;gap:12px;font-size:14.5px;font-weight:400;color:var(--ink);padding-bottom:9px;border-bottom:1px solid var(--line)}
.faq h4 i{width:25px;height:25px;border-radius:50%;background:var(--ink);color:#fff;font-style:normal;font-size:14px;font-weight:600;display:flex;align-items:center;justify-content:center;flex:none}
.faq p{font-size:11.5px;line-height:17.5px;color:var(--text);margin:12px 0 0 37px}

/* signup */
.signup{left:0;top:2507px;width:1200px;height:266px;background:linear-gradient(90deg,#1b1c1e 0%,#2c2d2f 50%,#6c6d6f 75%,#8a8b8d 100%)}
.signup h2{left:158px;top:78px;width:340px;font-size:27px;line-height:33px;font-weight:400;color:#fff}
.signup .btn{left:159px;top:162px;width:93px;height:33px}

/* footer */
.footer{left:0;top:2773px;width:1200px;height:180px;background:var(--footer)}
.footer-left{left:0;top:0;width:531px;height:180px;background:var(--footer-deep)}
.footer .brand{left:167px;top:50px;font-size:16px}
.footer-about{left:159px;top:82px;width:320px;font-size:10px;line-height:16px;color:#bfc0c2}
.fcol{top:40px;color:#fff}
.fcol h5{font-size:14.5px;font-weight:500;margin-bottom:12px}
.fcol a{display:block;font-size:10.5px;color:#c8c9cb;line-height:22.5px}
.legal{left:0;top:2953px;width:1200px;height:48px;background:var(--night)}
.social{left:160px;top:14px;display:flex;gap:9px}
.social span{width:21px;height:21px;border:1px solid #777;border-radius:50%}
.copy{right:152px;top:18px;font-size:9.5px;color:#bbb}
</style>
</head>
<body>

<section class="hero abs" role="img" aria-label="Black and white photo of a semi truck driving on a highway at dusk"></section>
<h1 class="hero-title abs">Best Industry Protection for Your shipment</h1>
<p class="hero-sub abs">All carriers working with us are required to have at least $100,000 in cargo liability insurance.</p>
<a class="btn btn-light hero-btn abs">GET A QUOTE</a>

<header class="site-header abs">
  <div class="brand abs"><span class="dot"></span>BLUESTONE FREIGHT</div>
  <nav class="nav abs">
    <a>Home</a><a>Carrier</a><a>Package</a>
    <span class="phone"><svg width="9" height="9" viewBox="0 0 24 24"><path fill="#fff" d="M6.6 10.8a15 15 0 006.6 6.6l2.2-2.2a1 1 0 011-.25 11.4 11.4 0 003.6.57 1 1 0 011 1V20a1 1 0 01-1 1A17 17 0 013 4a1 1 0 011-1h3.5a1 1 0 011 1c0 1.25.2 2.45.57 3.57a1 1 0 01-.25 1z"/></svg>555-014-2290</span>
  </nav>
  <svg class="search abs" width="12" height="12" viewBox="0 0 24 24"><circle cx="10" cy="10" r="7" stroke="#fff" stroke-width="3" fill="none"/><path d="M15 15l7 7" stroke="#fff" stroke-width="3"/></svg>
</header>

<section class="stats abs">
  <div class="stat">
    <svg width="30" height="30" viewBox="0 0 32 32" fill="none" stroke="#fff" stroke-width="1.5"><circle cx="16" cy="18" r="11"/><path d="M16 18V11M13 4h6M16 4v3"/></svg>
    <div><b>1,225</b><span>On Time Deliveries</span></div>
  </div>
  <div class="stat">
    <svg width="32" height="30" viewBox="0 0 32 30" fill="none" stroke="#fff" stroke-width="1.5"><path d="M4 24a12 12 0 1124 0"/><path d="M16 22l5-8"/><circle cx="16" cy="23" r="2"/></svg>
    <div><b>6,115</b><span>Miles per Week</span></div>
  </div>
  <div class="stat">
    <svg width="30" height="30" viewBox="0 0 32 32" fill="none" stroke="#fff" stroke-width="1.5"><rect x="3" y="14" width="6" height="14"/><path d="M9 15l6-10c2 0 3 1 3 3l-1 5h9a2 2 0 012 2l-2 10a2 2 0 01-2 2H9"/></svg>
    <div><b>105</b><span>Satisfied Customers</span></div>
  </div>
</section>

<h2 class="intro abs">Simple rates, real-time tracking, reliable service and<br><strong>outstanding customer support</strong></h2>

<div class="feature-card abs"></div>
<div class="feature abs" style="left:196px">
  <svg width="30" height="28" viewBox="0 0 30 28" fill="none" stroke="#111" stroke-width="1.4"><path d="M3 14a9 9 0 1 1 4 7.5L2 23l1.5-4.5A9 9 0 0 1 3 14z"/><path d="M16 7a8 8 0 0 1 9 12l1.5 4-4.5-1.5a8 8 0 0 1-8-1"/></svg>
  <h3>Instant capacity</h3>
  <p>Your trusted safe carrier is reliable, always growing, and always there for you.</p>
  <p class="tag">Heavy-Haul &amp; Flatbed</p>
</div>
<div class="feature abs" style="left:501px;width:200px">
  <svg width="42" height="28" viewBox="0 0 42 28" fill="none" stroke="#111" stroke-width="1.4"><rect x="1" y="3" width="24" height="17"/><path d="M25 8h9l6 7v5H25"/><circle cx="9" cy="22" r="3" fill="#fff"/><circle cx="33" cy="22" r="3" fill="#fff"/></svg>
  <h3>Freight at full speed</h3>
  <p>With simple instant quotes and booking, we eliminate time-consuming phone calls and email chains.</p>
  <p class="tag">Instant quote</p>
</div>
<div class="feature abs" style="left:792px;width:225px">
  <svg width="34" height="32" viewBox="0 0 34 32" fill="none" stroke="#111" stroke-width="1.4"><path d="M8 2a6 6 0 0 1 6 6c0 5-6 10-6 10S2 13 2 8a6 6 0 0 1 6-6z"/><circle cx="8" cy="8" r="2"/><path d="M8 20v4a4 4 0 0 0 4 4h12"/><circle cx="28" cy="26" r="4"/></svg>
  <h3>Real-time tracking</h3>
  <p>Real-time freight management lets you book and track loads online, day or night.</p>
  <p class="tag">Live shipment tracking</p>
</div>

<h2 class="price-title abs">$349.00 For Your DFW Dedicated Expedited 53’ Dry Van Truckload Freight</h2>
<div class="contact-row abs" style="left:240px;top:1201px">
  <span><svg width="9" height="9" viewBox="0 0 24 24"><path fill="#111" d="M6.6 10.8a15 15 0 006.6 6.6l2.2-2.2a1 1 0 011-.25 11.4 11.4 0 003.6.57 1 1 0 011 1V20a1 1 0 01-1 1A17 17 0 013 4a1 1 0 011-1h3.5a1 1 0 011 1c0 1.25.2 2.45.57 3.57a1 1 0 01-.25 1z"/></svg>555-014-2290</span>
  <span><svg width="12" height="9" viewBox="0 0 16 12" fill="none" stroke="#111" stroke-width="1.3"><rect x="1" y="1" width="14" height="10"/><path d="M1 1l7 6 7-6"/></svg>hello@bluestonefreight.com</span>
</div>
<a class="btn btn-dark abs" style="left:237px;top:1243px;width:94px;height:34px">GET A QUOTE</a>

<div class="map abs" role="img" aria-label="Map of Texas marking DFW, Austin and Houston"></div>
<div class="pin abs" style="left:813px;top:1110px"><svg width="12" height="17" viewBox="0 0 12 17"><path d="M6 0a6 6 0 0 1 6 6c0 4-6 11-6 11S0 10 0 6a6 6 0 0 1 6-6z" fill="#111"/><circle cx="6" cy="6" r="2.2" fill="#fff"/></svg><br>DFW</div>
<div class="pin abs" style="left:796px;top:1194px"><svg width="12" height="17" viewBox="0 0 12 17"><path d="M6 0a6 6 0 0 1 6 6c0 4-6 11-6 11S0 10 0 6a6 6 0 0 1 6-6z" fill="#111"/><circle cx="6" cy="6" r="2.2" fill="#fff"/></svg><br>Austin</div>
<div class="pin abs" style="left:897px;top:1207px"><svg width="12" height="17" viewBox="0 0 12 17"><path d="M6 0a6 6 0 0 1 6 6c0 4-6 11-6 11S0 10 0 6a6 6 0 0 1 6-6z" fill="#111"/><circle cx="6" cy="6" r="2.2" fill="#fff"/></svg><br>Hoston</div>
<div class="map-card abs">
  <h4>Austin</h4>
  <p><svg width="9" height="12" viewBox="0 0 12 17" style="flex:none"><path d="M6 0a6 6 0 0 1 6 6c0 4-6 11-6 11S0 10 0 6a6 6 0 0 1 6-6z" fill="#111"/></svg>Austin is the state capital of Texas, an inland city</p>
  <p><svg width="8" height="8" viewBox="0 0 24 24" style="flex:none;margin-top:3px"><path fill="#111" d="M6.6 10.8a15 15 0 006.6 6.6l2.2-2.2a1 1 0 011-.25 11.4 11.4 0 003.6.57 1 1 0 011 1V20a1 1 0 01-1 1A17 17 0 013 4a1 1 0 011-1h3.5a1 1 0 011 1c0 1.25.2 2.45.57 3.57a1 1 0 01-.25 1z"/></svg>555-014-2290</p>
  <p style="font-size:8px"><svg width="10" height="8" viewBox="0 0 16 12" fill="none" stroke="#111" stroke-width="1.3" style="flex:none;margin-top:3px"><rect x="1" y="1" width="14" height="10"/><path d="M1 1l7 6 7-6"/></svg>hello@bluestonefreight.com</p>
</div>

<h2 class="value-title abs">A Unique Value Addition to Your Logistics Strategy</h2>
<ul class="value-list abs">
  <li>Highest Safety Standards and Score.</li>
  <li>On-Time Every Time</li>
  <li>Outstanding Customer Service Team</li>
  <li>Online Load Traking</li>
  <li>Automated Easy Booking System.</li>
  <li>Specilized DFW Expeidted Freight.</li>
  <li>Heavy-Haul, Flatbed and Dry Van Freight.</li>
</ul>
<div class="value-shadow abs"></div>
<div class="value-photo abs" role="img" aria-label="Black and white photo of a semi truck on an open road with mountains behind"></div>

<div class="testi-band abs"></div>
<h2 class="testi-title abs">Testimonials</h2>
<a class="view-all abs">View all</a>
<article class="quote abs" style="left:158px">
  <p>“As soon as we hit our busy season, it was incredibly helpful to have the extra capacity Harlow Logistics provides.”</p>
  <hr>
  <div class="person"><span class="avatar"></span><div><b>Dana Merritt</b><small>Distribution Manager</small></div></div>
</article>
<article class="quote abs" style="left:461px">
  <p>“I can’t tell you how much easier my life got the very minute I used simple online Auotmate ordering system first time.”</p>
  <hr>
  <div class="person"><span class="avatar" style="background:#3a3b3d"></span><div><b>Owen Castell</b><small>VP of Operations</small></div></div>
</article>
<article class="quote abs" style="left:757px">
  <p>“Harlow Logistics is our go to Company when the load must get there safely no excuses on-time”</p>
  <hr>
  <div class="person"><span class="avatar" style="background:#1e5f9e"></span><div><b>Priya Navarro</b><small>Logistics Manager</small></div></div>
</article>

<h2 class="faq-title abs">Frequently asked questions</h2>
<div class="faq abs" style="left:160px;top:2256px;width:388px">
  <h4><i>?</i>Your business is our business</h4>
  <p>We’re building solutions to deliver peak efficiency and flexibility in your supply chain, backed by dedicated account managers and outstanding support.</p>
</div>
<div class="faq abs" style="left:160px;top:2379px;width:400px">
  <h4 style="width:388px"><i>?</i>What support do you provide?</h4>
  <p>We provide shippers with outstanding phone support to address any problems or concerns, from setup to management.</p>
</div>
<div class="faq abs" style="left:608px;top:2256px;width:392px">
  <h4><i>?</i>What Information is available?</h4>
  <p>Details on all future, present, and past loads are kept directly in our platform. This includes necessary documents, such as PODs uploaded by carriers. We also provide real-time GPS tracking on loads when available, instant Simple marketplace pricing, and performance metrics around operations at your facilities.</p>
</div>

<section class="signup abs" role="img" aria-label="Black and white photo of a smiling warehouse worker in a cap and safety vest holding a package">
  <h2 class="abs">Sign up for free and start shipping today</h2>
  <a class="btn btn-light abs">SIGN UP</a>
</section>

<footer class="footer abs">
  <div class="footer-left abs"></div>
  <div class="brand abs"><span class="dot"></span>BLUESTONE FREIGHT</div>
  <p class="footer-about abs">Lorem Ipsum is simply dummy text of the printing and typesetting industry. Lorem Ipsum has been the industry’s standard dummy text ever since the 1500s, when an unknown printer took a galley of type and scrambled</p>
  <div class="fcol abs" style="left:677px"><h5>Get Started</h5><a>Resources</a><a>Tutorials</a><a>Examples</a><a>Docs</a></div>
  <div class="fcol abs" style="left:823px"><h5>About</h5><a>Stories</a><a>Community</a><a>Blog</a><a>Brand Assets</a></div>
  <div class="fcol abs" style="left:972px"><h5>Features</h5><a>Overview</a><a>Design</a><a>Code</a><a>Collaborate</a></div>
</footer>
<div class="legal abs">
  <div class="social abs"><span></span><span></span><span></span></div>
  <p class="copy abs">Copyright All rights reserved.</p>
</div>

</body>
</html>
```